Tradeway Markets Company is looking for a web page design

Your projects should contain:

1. Header: Logo provided by us.
2. Top nav bar: offer, about us, experience, contact.
3. “Choose language” button.
4. Main section: panoramic picture (static, professional, modern).
5. Below section: 3 blocks (image+title+description), which represent our 3 main activities (titles):
• Market Research,
• Marketing Plans,
• Marketing Project.
6. ‘Contact us’ form – Message (text: “Write your message and give us details about your company and activities”), Email, SEND).
7. Page footer: (4 section: Contact, Social Media, Blog, Partners).
Updates

Hello!

I uploaded new file 'general_look', which is our idea how the page should generally look like.

BUT! it doesn't mean that your projects should look exactly like this project e.g.:
* titles Market Research, Marketing Plans, Marketing Project can be above these: Image 1,2,3.
* everything doesn't have to be in square and rectangle shape. You can try to manipulate with blocks and can add elipse elemnts or something similar.

We will appreciate your innovative ideas. Just wanted to give you general plan of the site and ilustrate all elements that we require.

Best Regards,
Teodor

IMPORTENT

Please remember that the main picture should be panoramic. Please do not close it in frame.

Target Market(s)

Small and middle sized companies, which would like to export their goods and services abroad and are interested in raising funds from Coastal Alliance to expand their activities. These are rather industrial companies with low level of innovativeness. Our mission is to build image of the client’s company and increase awareness of their products to improve their competitiveness and innovativeness.

Industry/Entity Type

It Company

Requirements
Must have
• 1. Create designs of main page and subpage.
2. Subpage: Logo, Header, language button, place for article, navigation menu on the right side - below it “contact us” button , footer on the bottom. (In this section we are looking mainly for the design of the header and navigation menu).
3. The whole design should be a series of horizontal blocks.
4. Your projects should be associated with features such as: Reliability, Security, Professionalism, Openness, Uniqueness.
5. The design should be simple, fresh, readable, easy to use and should create a feeling of high quality services.
6. Possibility to change the panoramic picture (separate layer in a graphic file).
7. All pictures and blocks should be static, no movements.
8. Style of the page should be compliant with the logo design, font: Swiss.
9. Designs that we like: http://www.brixomedia.pl/, http://www.zentrofalu.com/.
Should not have
• There shouldn’t be any distractions and not matching parts (whole design should be compact and easy to interpret and remember).

```html
<!DOCTYPE html>
<html lang="en">
<head>
<meta charset="utf-8">
<title>Tradeway Markets</title>
<link href="https://fonts.googleapis.com/css2?family=Arimo:wght@400;700&family=Open+Sans:wght@400;600;700&family=Oswald:wght@600;700&family=Noto+Serif&display=swap" rel="stylesheet">
<style>
  :root{
    --page:#f1f1f1;
    --ink:#222;
    --ink-soft:#3a3a3a;
    --brand:#1f5f8b;
    --brand-light:#4a87b3;
    --brand-dark:#174a6c;
    --nav:#3d3d3d;
    --field:#444;
    --hero-bg:#e8ecef;
    --footer:#121212;
    --white:#fff;
    --search:#d3d3d3;
  }
  *{box-sizing:border-box;margin:0;padding:0}
  html,body{width:911px;height:1200px;overflow:hidden}
  body{background:var(--page);font-family:"Open Sans",Arial,sans-serif;color:var(--ink);position:relative}
  .abs{position:absolute}

  .brand{left:123px;top:30px}
  .brand-name{display:block;font-family:"Arimo",Arial,sans-serif;font-weight:700;font-size:33px;line-height:36px;color:var(--brand)}
  .brand-tagline{display:block;margin-top:4px;font-family:"Arimo",Arial,sans-serif;font-weight:700;font-size:11px;line-height:13px;color:var(--brand)}

  .lang{right:122px;top:17px;font-size:13px;display:flex;gap:14px;color:var(--ink)}
  .search{left:564px;top:43px;display:flex}
  .search-field{width:161px;height:33px;background:var(--search)}
  .search-btn{width:64px;height:33px;background:linear-gradient(var(--brand-light),var(--brand-dark));color:var(--white);font-weight:700;font-size:12px;display:flex;align-items:center;justify-content:center}

  .nav{left:123px;top:108px;width:666px;height:67px;background:var(--nav);display:flex;align-items:center}
  .nav a{font-family:"Oswald",Arial,sans-serif;font-weight:700;font-size:26px;color:var(--white);text-decoration:none;height:100%;display:flex;align-items:center}
  .nav .active{background:linear-gradient(var(--brand-light),var(--brand-dark));width:120px;padding-left:13px}
  .nav .item-about{margin-left:31px}
  .nav .item-exp{margin-left:78px}
  .nav .item-contact{margin-left:83px}

  .hero{left:123px;top:175px;width:666px;height:274px;background:var(--hero-bg);overflow:hidden}
  .hero-photo{position:absolute;left:0;top:0;width:260px;height:274px;background:linear-gradient(90deg,#d9c3b7,#e6dcd6 70%,var(--hero-bg))}
  .hero-title{position:absolute;left:276px;top:55px;font-family:"Arimo",Arial,sans-serif;font-weight:700;font-size:27px;color:var(--ink-soft);letter-spacing:-0.5px;text-shadow:1px 1px 1px rgba(0,0,0,.25)}
  .hero-text{position:absolute;left:277px;top:97px;width:270px;font-family:"Noto Serif",Georgia,serif;font-size:13.5px;line-height:19px;color:#555}
  .hero-btn{position:absolute;left:277px;top:178px;width:148px;height:43px;background:var(--ink-soft);color:var(--white);font-weight:700;font-size:14px;display:flex;align-items:center;justify-content:center}
  .hero-dots{position:absolute;left:570px;top:250px;display:flex;gap:6px}
  .hero-dots span{width:18px;height:18px;border-radius:50%;background:var(--ink-soft)}

  .service{top:472px;width:220px;text-align:center}
  .service-photo{width:208px;height:208px;margin:0 auto;border-radius:50%;border:4px solid var(--white);box-shadow:0 0 6px rgba(0,0,0,.3)}
  .photo-research{background:radial-gradient(circle,#e8eaea,#b9c2c0)}
  .photo-plan{background:radial-gradient(circle,#f2f2f0,#c8cdd0)}
  .photo-project{background:radial-gradient(circle,#d8e0ea,#8ea4bd)}
  .service-title{font-family:"Arimo",Arial,sans-serif;font-weight:700;font-size:18px;color:var(--ink-soft);margin-top:9px}
  .service-text{font-size:12.3px;line-height:15px;margin-top:4px;color:var(--ink)}
  .more-btn{display:inline-block;width:77px;height:27px;line-height:27px;margin-top:14px;background:linear-gradient(var(--brand-light),var(--brand-dark));color:var(--white);font-weight:700;font-size:13px}

  .section-title{font-family:"Arimo",Arial,sans-serif;font-weight:700;font-size:18px;color:var(--ink-soft);letter-spacing:-0.5px}
  .field{background:var(--field);color:var(--white);font-weight:700;font-size:12.5px;padding:6px 4px}
  .send-btn{left:228px;top:1003px;width:87px;height:33px;background:linear-gradient(var(--brand-light),var(--brand-dark));color:var(--white);font-weight:700;font-size:13px;display:flex;align-items:center;justify-content:center}

  .contact-info{left:553px;top:852px;font-size:13px;line-height:16px;color:var(--ink)}
  .contact-info p{margin-bottom:11px}
  .contact-info .web{font-style:italic}
  .contact-icons{left:600px;top:986px;display:flex;align-items:center;gap:12px;font-weight:700;font-size:13px;color:var(--ink-soft)}

  .footer{left:123px;top:1053px;width:666px;height:147px;background:var(--footer);color:var(--white)}
  .footer-col{position:absolute;top:6px}
  .footer-col h3{font-family:"Oswald",Arial,sans-serif;font-weight:700;font-size:15px;line-height:22px;letter-spacing:.2px}
  .footer-col li{list-style:none;font-weight:700;font-size:11.5px;height:21.5px;display:flex;align-items:center;gap:3px}
  .footer-col li::before{content:"";width:6px;height:6px;border-top:2px solid var(--brand-light);border-right:2px solid var(--brand-light);transform:rotate(45deg);margin-right:3px}
  .social li{height:27px}
  .social-square{width:22px;height:22px;border-radius:3px;background:var(--brand-light);margin-left:6px}
</style>
</head>
<body>

<header>
  <div class="brand abs">
    <span class="brand-name">Tradeway Markets</span>
    <span class="brand-tagline">your route to markets abroad</span>
  </div>
  <div class="lang abs"><span>English</span><span>Polish</span></div>
  <div class="search abs"><div class="search-field"></div><div class="search-btn">SEARCH</div></div>
</header>

<nav class="nav abs">
  <a class="active" href="#">Offer</a>
  <a class="item-about" href="#">About Us</a>
  <a class="item-exp" href="#">Experience</a>
  <a class="item-contact" href="#">Contact Us</a>
</nav>

<section class="hero abs">
  <div class="hero-photo" role="img" aria-label="Portrait of a smiling businesswoman"></div>
  <h1 class="hero-title">Lorem ipsum dolor sit amet</h1>
  <p class="hero-text">Sed ut perspiciatis unde omnis iste natus error sit voluptatem accusantium doloremque laudan.</p>
  <div class="hero-btn">CLICK FOR MORE</div>
  <div class="hero-dots"><span></span><span></span><span></span></div>
</section>

<section class="service abs" style="left:119px">
  <div class="service-photo photo-research" role="img" aria-label="Hands reviewing bar charts with a pen"></div>
  <h2 class="service-title">Market Research</h2>
  <p class="service-text">At vero eos et accusamus et iusto odio dignissimos ducimus qui blanditiis praesentium voluptatum</p>
  <span class="more-btn">MORE</span>
</section>
<section class="service abs" style="left:346px">
  <div class="service-photo photo-plan" role="img" aria-label="Business people pointing at pie charts on paper"></div>
  <h2 class="service-title">Marketing Plan</h2>
  <p class="service-text">At vero eos et accusamus et iusto odio dignissimos ducimus qui blanditiis praesentium voluptatum</p>
  <span class="more-btn">MORE</span>
</section>
<section class="service abs" style="left:575px">
  <div class="service-photo photo-project" role="img" aria-label="Pen resting on a project document"></div>
  <h2 class="service-title">Marketing Project</h2>
  <p class="service-text">At vero eos et accusamus et iusto odio dignissimos ducimus qui blanditiis praesentium voluptatum.</p>
  <span class="more-btn">MORE</span>
</section>

<section class="message">
  <h2 class="section-title abs" style="left:122px;top:822px">Message Us</h2>
  <div class="field abs" style="left:123px;top:853px;width:157px;height:27px">Your Name</div>
  <div class="field abs" style="left:285px;top:853px;width:158px;height:27px">Your Email Address</div>
  <div class="field abs" style="left:123px;top:889px;width:320px;height:104px;padding-top:20px">Your Message</div>
  <div class="send-btn abs">SEND</div>
</section>

<section class="contact">
  <h2 class="section-title abs" style="left:568px;top:822px">Contact Us</h2>
  <div class="contact-info abs">
    <p>Email: info@tradewaymarkets.com</p>
    <p>Address: Tradeway Markets Company,<br>Strreetname: 123 Poland.</p>
    <p>&nbsp;Ph: 000 - 111 - 222</p>
    <p class="web">www.tradewaymarkets.com</p>
  </div>
  <div class="contact-icons abs">
    <svg width="47" height="28" viewBox="0 0 47 28" aria-hidden="true"><rect width="47" height="28" fill="#1f5f8b"/><path d="M1 1 L23.5 17 L46 1" fill="none" stroke="#f1f1f1" stroke-width="2"/><path d="M1 27 L18 13 M46 27 L29 13" stroke="#f1f1f1" stroke-width="1.5"/></svg>
    <span>OR</span>
    <svg width="40" height="30" viewBox="0 0 40 30" aria-hidden="true"><path d="M2 10 Q20 -2 38 10 L36 14 L29 12 L28 8 Q20 5 12 8 L11 12 L4 14 Z" fill="#1f5f8b"/><path d="M8 30 L12 14 L28 14 L32 30 Z" fill="#1f5f8b"/><circle cx="20" cy="22" r="4" fill="#f1f1f1"/></svg>
  </div>
</section>

<footer class="footer abs">
  <div class="footer-col" style="left:12px">
    <h3>PARTNERS</h3>
    <ul><li>DOLOREMQUE</li><li>DOLOREMQUE</li><li>DOLOREMQUE</li><li>DOLOREMQUE</li><li>DOLOREMQUE</li></ul>
  </div>
  <div class="footer-col" style="left:193px">
    <h3>BLOG</h3>
    <ul><li>DOLOREMQUE</li><li>DOLOREMQUE</li><li>DOLOREMQUE</li><li>DOLOREMQUE</li><li>DOLOREMQUE</li></ul>
  </div>
  <div class="footer-col social" style="left:368px">
    <h3>SOCIAL MEDIA</h3>
    <ul><li><span class="social-square"></span></li><li><span class="social-square"></span></li><li><span class="social-square"></span></li></ul>
  </div>
  <div class="footer-col" style="left:558px">
    <h3>CONTACT US</h3>
    <ul><li>EMAIL</li><li>ADDRESS</li><li>PH NUMBER</li></ul>
  </div>
</footer>

</body>
</html>
```